Business Card Design

Velora Pixel Outreach

An online marketing consulting & strategy business for the cosmetic niche

We specialise in Increasing Leads, Conversions & Content Marketing

I am looking for a very clean, BOLD business card that is simple & effective

Target Market(s)

cosmetic surgeons & cosmetic clinics

Industry/Entity Type

Marketing

Contact Information for Business Card

Brett Kaminski
Online Marketing Strategist

Brett@VeloraPixelOutreach.example
0491 268 530

LinkedIn: in/brettkaminski

```html
<!DOCTYPE html>
<html lang="en">
<head>
<meta charset="utf-8">
<title>Velora Pixel Outreach – Business Card</title>
<link rel="stylesheet" href="https://fonts.googleapis.com/css2?family=Michroma&family=Lusitana:wght@700&family=Courier+Prime&family=Tinos&display=swap">
<style>
  :root {
    --page-bg: #dfe9ee;
    --band-deep: #1297bf;
    --band-mid: #1eb0d6;
    --band-light: #6fd0ea;
    --card-white: #fbfcfd;
    --ink-grey: #4b5056;
    --ink-dark: #2f3338;
    --mark-teal: #27a9c4;
    --accent-green: #9fd23a;
    --accent-violet: #7b5aa6;
  }
  * { box-sizing: border-box; margin: 0; padding: 0; }
  html, body {
    width: 1200px; height: 741px; overflow: hidden;
    background: var(--page-bg);
  }
  .sheet {
    position: relative; width: 1200px; height: 741px;
    display: flex; align-items: center; justify-content: center; gap: 60px;
  }
  .card {
    position: relative; width: 520px; height: 314px;
    background: var(--card-white);
    box-shadow: 0 10px 30px rgba(20, 70, 100, 0.18);
    overflow: hidden;
  }
  .card__band {
    position: absolute; left: 0; right: 0;
    background: linear-gradient(90deg, var(--band-deep) 0%, var(--band-mid) 55%, var(--band-light) 100%);
  }
  .card__band--top { top: 0; height: 60px; }
  .card__band--bottom { bottom: 0; height: 60px; background: linear-gradient(90deg, var(--band-deep) 0%, var(--band-mid) 70%, var(--band-light) 100%); }
  .card__flourish {
    position: absolute; width: 70px; height: 34px;
  }
  .card__flourish--top { top: 0; right: 0; background: linear-gradient(200deg, var(--accent-violet) 0%, var(--accent-green) 45%, rgba(111,208,234,0) 100%); }
  .card__flourish--bottom { bottom: 6px; right: 0; background: linear-gradient(160deg, rgba(111,208,234,0) 0%, var(--accent-green) 70%, #e3f27a 100%); height: 24px; }

  .brand {
    display: flex; align-items: center; gap: 12px;
  }
  .brand__dot {
    width: 50px; height: 50px; border-radius: 50%;
    background: var(--mark-teal); flex: none;
  }
  .brand__name {
    font-family: "Michroma", sans-serif;
    font-size: 20px; line-height: 1.08;
    color: var(--ink-grey); text-transform: uppercase;
    letter-spacing: 0.5px;
  }

  .card--front .brand { position: absolute; left: 50px; top: 122px; }
  .contact {
    position: absolute; left: 322px; top: 98px;
  }
  .contact__name, .contact__role {
    font-family: "Lusitana", serif; font-weight: 700;
    font-size: 13px; line-height: 22px; letter-spacing: 1px;
    color: var(--ink-dark); text-transform: uppercase;
  }
  .contact__lines {
    margin-top: 24px;
    font-family: "Courier Prime", monospace;
    font-size: 10px; line-height: 13px; color: var(--ink-dark);
  }

  .card--back .brand {
    position: absolute; left: 50%; top: 122px; transform: translateX(-50%);
  }
  .card__email {
    position: absolute; left: 0; right: 0; top: 205px; text-align: center;
    font-family: "Tinos", serif; font-size: 13px; color: var(--ink-grey);
  }
</style>
</head>
<body>
<main class="sheet">
  <section class="card card--front">
    <div class="card__band card__band--top"></div>
    <div class="card__flourish card__flourish--top" role="img" aria-label="Colourful abstract swoosh accent"></div>
    <div class="brand">
      <span class="brand__dot"></span>
      <p class="brand__name">Velora<br>Pixel<br>Outreach</p>
    </div>
    <div class="contact">
      <p class="contact__name">Brett Kaminski</p>
      <p class="contact__role">Online Marketing<br>Strategist</p>
      <p class="contact__lines">c: 0491 268 530<br>LinkedIn: in/brettkaminski</p>
    </div>
    <div class="card__band card__band--bottom"></div>
    <div class="card__flourish card__flourish--bottom" role="img" aria-label="Colourful abstract swoosh accent"></div>
  </section>

  <section class="card card--back">
    <div class="card__band card__band--top"></div>
    <div class="card__flourish card__flourish--top" role="img" aria-label="Colourful abstract swoosh accent"></div>
    <div class="brand">
      <span class="brand__dot"></span>
      <p class="brand__name">Velora<br>Pixel<br>Outreach</p>
    </div>
    <p class="card__email">Brett@VeloraPixelOutreach.example</p>
    <div class="card__band card__band--bottom"></div>
    <div class="card__flourish card__flourish--bottom" role="img" aria-label="Colourful abstract swoosh accent"></div>
  </section>
</main>
</body>
</html>
```